A compelling brochure for a children's charity to encourage donations

We are looking for a 4-page A-4 booklet (1 x A3 page folded in half). the Lantern Harbour Foundation is a non-profit organisation that aims to reduce the incidence and impact of children's critical injury in Australia. The brochure will give people who are new to the charity, an overview of who we are, what we do, why we do it and how they can help. You can reference our website www.lanternharbourkids.org.au for colours and styles. The final design should encourage people to make a donation by being positive and powerful.
Use the text in the uploaded files.

```html
<!DOCTYPE html>
<html lang="en">
<head>
<meta charset="utf-8">
<title>Lantern Harbour Foundation – Back Cover</title>
<link rel="stylesheet" href="https://fonts.googleapis.com/css2?family=Noto+Serif:wght@400&display=swap">
<style>
  :root {
    --magenta: #c200bf;
    --magenta-deep: #b300b3;
    --text-light: #ffffff;
  }
  html, body {
    margin: 0;
    padding: 0;
    overflow: hidden;
  }
  .back-cover {
    position: relative;
    width: 848px;
    height: 1200px;
    overflow: hidden;
    font-family: "Noto Serif", Georgia, serif;
    color: var(--text-light);
  }
  .back-cover__texture {
    position: absolute;
    inset: 0;
    background: linear-gradient(160deg, var(--magenta) 0%, var(--magenta-deep) 50%, var(--magenta) 100%);
  }
  .back-cover__cta {
    position: absolute;
    left: 0;
    right: 0;
    top: 538px;
    text-align: center;
  }
  .cta__invite {
    margin: 0;
    font-size: 20px;
    line-height: 1.2;
    font-weight: 400;
  }
  .cta__web {
    margin: 6px 0 0;
    font-size: 40px;
    line-height: 1.2;
    font-weight: 400;
    letter-spacing: 0.2px;
  }
</style>
</head>
<body>
  <main class="back-cover">
    <div class="back-cover__texture" role="img" aria-label="Magenta diamond lattice pattern covering the whole page"></div>
    <section class="back-cover__cta">
      <p class="cta__invite">Join our journey</p>
      <p class="cta__web">www.lanternharbourkids.org.au</p>
    </section>
  </main>
</body>
</html>
```